Our private family owned investment company owns a vineyard in Napa. We want to design a label to put on our wine bottles once wine is ready. We would like artists to develop a creative design for a new label using this wording: Vineyard 48217. The dimensions of the label will be the standard label size on a 750 ml wine bottle. We appreciate creative flair, a classy look, preferably color but open to black and white too; maybe submit both ways. **As more explanation for designers, our family founded and owned a business for over 50 years and our logo was a teal colored snowflake (see attached jpeg logo). Our first plant address was numbered 48217. After our business was sold, our new family office is on located at 48217 Holloway. We have created a new business logo (see attached blue TRV logo) So the 48217 and 2 logos all have lineage and sentimental value to our family. Thank you for providing your unique creativity to this project.

Target Market(s)

to inspire conversation and reminiscing among friends and business associates when entertaining them.

Industry/Entity Type

Investment

Colors

Designer to choose colors to be used in the design.

Requirements
Must have
• Must Incorporate the wording: Vineyard 48217 - as part of the entire design and please see the attached logos (sketch of Vineyard 48217, blue snowflake logo, and TRV logo) and use any of these as a base, or part of, your new design. ** See project description for more detail on the meaning behind these logos.**

```html
<!DOCTYPE html>
<html lang="en">
<head>
<meta charset="utf-8">
<title>Vineyard 48217 — Wine Label</title>
<link rel="stylesheet" href="https://fonts.googleapis.com/css2?family=Poppins:wght@400;600&display=swap">
<style>
  :root {
    --backdrop: #cdc8c9;
    --label-paper: #f7f7f6;
    --ink: #1b1b1b;
    --rule: #2a2a2a;
  }
  * { margin: 0; padding: 0; box-sizing: border-box; }
  html, body {
    width: 1200px;
    height: 900px;
    overflow: hidden;
    background: var(--backdrop);
  }
  .canvas {
    width: 1200px;
    height: 900px;
    display: flex;
    align-items: center;
    justify-content: center;
  }
  .wine-label {
    position: relative;
    width: 520px;
    height: 650px;
    background: var(--label-paper);
    box-shadow: 0 2px 10px rgba(0, 0, 0, 0.08);
  }
  .label-content {
    position: absolute;
    left: 125px;
    top: 72px;
    width: 270px;
    height: 428px;
    display: flex;
    flex-direction: column;
  }
  .rule {
    height: 2px;
    background: var(--rule);
    flex: none;
  }
  .brand-name {
    flex: 1;
    display: flex;
    flex-direction: column;
    justify-content: center;
    font-family: "Poppins", sans-serif;
    font-weight: 600;
    font-size: 58px;
    line-height: 1.2;
    color: var(--ink);
    text-align: center;
  }
  .brand-name span { display: block; }
  .volume {
    position: absolute;
    left: 0;
    right: 0;
    top: 524px;
    font-family: "Poppins", sans-serif;
    font-weight: 400;
    font-size: 17px;
    color: var(--ink);
    text-align: center;
  }
</style>
</head>
<body>
  <main class="canvas">
    <section class="wine-label" aria-label="Vineyard 48217 wine label">
      <div class="label-content">
        <div class="rule"></div>
        <h1 class="brand-name"><span>Vineyard</span><span>48217</span></h1>
        <div class="rule"></div>
      </div>
      <p class="volume">750ml</p>
    </section>
  </main>
</body>
</html>
```